AMAZING WEBSITE DESIGN NEEDED FOR MAID / CLEANING SERVICE

NOTE: This is Website Design Only - No coding required

Please submit your designs ASAP as we want to pick a winner and get started!

Hey,

We are looking for a new amazing website design for a maid or cleaning service.

They have a horrible website that we want turned into a masterpiece.

As you will see on their current site:

http://tidyhavenco.examplehost.net/

They have a lot of stuff, very disorganized, and need help.

Here is what we need:

Colors: Same as current site, Orange, Gray, Black

Menu: Horizontal with same Menu items

Need a spot for a video on the homepage

Want content to be structured in a great format that is easy to read.

Want to highlight commercial and residential on the website homepage.

Also want a spot for customer testimonials

We want the site clean, professional, fresh and modern.

Please help by matching the logo design.

I look forward to your designs!
Updates

Hi All! Really appreciate your efforts and designs. I will be meeting with our client on Monday and will then be able to provide feedback after our meeting. If you have other ideas, please submit them. The more I can show him the better! Thanks!

Target Market(s)

The target market is residential home owners as well as commercial businesses who need cleaning on a regular basis.

This company cleans homes and offices for individuals.

Industry/Entity Type

Residential

Font styles to use
Sans Serif

Requirements
Must have
• Must match logo colors
Must have spot for video
Must have a clean look
Must have a bold look
Nice to have
• Highly visual
Should not have
• clutter
messy design
hard to read

```html
<!DOCTYPE html>
<html lang="en">
<head>
<meta charset="utf-8">
<title>Tidy Haven — Quality Commercial &amp; Residential Cleaning</title>
<link href="https://fonts.googleapis.com/css2?family=Open+Sans:wght@400;600;700&display=swap" rel="stylesheet">
<style>
:root{
  --orange:#f7941d;
  --charcoal:#3b3b3b;
  --ink:#2b2b2b;
  --text:#777;
  --light:#f2f2f2;
  --rule:#e2e2e2;
  --footer:#3a3a3a;
  --footer-bottom:#262626;
  --white:#fff;
}
*{box-sizing:border-box;margin:0;padding:0}
html,body{width:906px;height:1200px;overflow:hidden;background:var(--white)}
body{font-family:"Open Sans",Arial,sans-serif;color:var(--text);font-size:6.4px;line-height:1.4}
.page{position:relative;width:906px;height:1200px;overflow:hidden}
.abs{position:absolute}
.topbar{left:0;top:0;width:906px;height:4px;background:var(--orange)}

.brand{left:234px;top:40px;display:flex;align-items:center;gap:8px}
.brand-mark{width:30px;height:30px;background:var(--orange)}
.brand-name{font-size:22px;font-weight:700;color:var(--charcoal);letter-spacing:-.5px;line-height:1}
.brand-tag{left:252px;top:78px;font-size:6.5px;font-style:italic;color:var(--text)}

.callout{right:230px;top:26px;text-align:right;font-size:6.5px;color:#999;line-height:1.3}
.callout .phone{display:block;margin-top:4px;font-size:11px;font-weight:600;color:var(--orange)}
.search{left:592px;top:64px;width:84px;height:19px;border:1px solid var(--rule);display:flex;align-items:center;gap:5px;padding-left:7px;font-size:6px;color:#aaa}

.hero{left:0;top:113px;width:906px;height:197px;background:linear-gradient(90deg,#e8dccb 0%,#c9b196 35%,#b99b78 55%,#5dbfc6 75%,#2aa9b4 100%)}
.nav{left:234px;top:101px;width:442px;height:23px;background:var(--charcoal);display:flex;align-items:center;justify-content:space-around;padding:0 6px;z-index:2}
.nav a{color:#ddd;text-decoration:none;font-size:6.2px;white-space:nowrap}
.nav a.current{color:var(--orange)}
.hero-caption{right:230px;top:218px;text-align:right}
.hero-caption span{display:inline-block;background:var(--orange);color:var(--white);font-size:11px;line-height:1.5;padding:0 6px;margin-bottom:2px}

h2{font-size:10px;line-height:14px;font-weight:400;color:var(--ink);text-transform:uppercase;letter-spacing:.3px}
h2 em{font-style:normal;color:var(--orange)}

.about{left:234px;top:324px;width:270px}
.about p{margin-top:6px;line-height:9px}
.more{position:absolute;left:0;top:100px;color:var(--orange);font-size:6px}
.video-title{left:518px;top:324px}
.video{left:520px;top:344px;width:156px;height:88px;background:#111;padding:4px}
.video-frame{width:100%;height:68px;background:linear-gradient(135deg,#d9c39a,#a4784a)}
.video-bar{display:flex;align-items:center;gap:5px;height:12px}
.video-bar .track{flex:1;height:2px;background:#555}

.band{left:234px;top:452px;width:442px;height:27px;background:var(--orange);color:var(--white);font-size:8px;display:flex;align-items:center;padding-left:11px}

.service{top:496px;width:102px}
.service .thumb{height:72px;border:3px solid var(--white);box-shadow:0 1px 3px rgba(0,0,0,.25)}
.service h3{margin-top:9px;font-size:7.4px;line-height:10px;font-weight:700;color:var(--orange);white-space:nowrap}
.service p{margin-top:2px;font-size:6px;line-height:8.4px}
.service.promo{width:106px}
.service.promo .thumb{border-color:var(--orange);height:74px}
.service.promo h3{margin-top:7px}
.service.promo p{color:var(--orange)}
.service.promo strong{display:block;margin-top:6px;color:var(--orange);font-size:6.4px;line-height:8.6px}

.rule{left:234px;width:442px;height:1px;background:var(--rule)}

.clients{left:234px;top:668px;width:442px}
.slider{position:absolute;right:0;top:3px;display:flex;gap:2px}
.slider span{width:8px;height:8px;background:#ddd}
.quote{margin-top:7px;background:var(--light);height:54px;position:relative}
.quote p{position:absolute;left:28px;top:11px;right:20px;font-size:6.4px;line-height:9px}
.quote svg{position:absolute;left:9px;top:12px}
.quote footer{position:absolute;left:0;bottom:0;width:100%;height:15px;background:#e6e6e6;padding:3px 9px;font-size:6.4px;color:var(--ink);font-weight:600}
.quote footer i{font-weight:400;color:var(--text)}

.offer{top:768px}
.offer p{margin-top:8px;line-height:9px}
.offer ul{list-style:none;margin-top:10px}
.offer li{font-size:6.2px;line-height:10.8px;padding-left:12px;position:relative}
.offer li::before{content:"";position:absolute;left:0;top:3.5px;border-left:4px solid var(--orange);border-top:2px solid transparent;border-bottom:2px solid transparent}

.pledges{left:234px;top:924px;width:442px;height:51px;background:var(--charcoal);display:flex;align-items:center}
.pledge{flex:1;display:flex;align-items:center;gap:9px;padding:0 9px;color:#ccc;font-size:6.2px;line-height:1.35}
.pledge+.pledge{border-left:1px solid #555}
.pledge b{color:var(--orange)}
.pledge .badge{flex:none;width:28px;height:28px;border-radius:50%;background:#888}
.up{left:448px;top:991px;width:14px;height:14px;border-radius:50%;background:var(--charcoal)}

.footer{left:0;top:1021px;width:906px;height:141px;background:var(--footer);color:#bbb}
.footer h4{font-size:6.8px;font-weight:700;color:var(--white);text-transform:uppercase}
.footer h4 em{font-style:normal;color:var(--orange)}
.fcol{position:absolute;top:20px;font-size:6.2px}
.fcol .time{display:block;font-size:5px;color:#888;margin-bottom:6px}
.fcol .link{color:var(--orange)}
.fcol .row{display:flex;align-items:flex-start;gap:8px;margin-top:6px}
.fcol .dot{flex:none;width:7px;height:7px;background:var(--orange)}
.copy{left:0;top:1162px;width:906px;height:38px;background:var(--footer-bottom);padding:13px 234px 0;font-size:6px;color:#bbb}
.copy a{color:#bbb;text-decoration:none}
.copy a.current{color:var(--orange)}
.copy small{display:block;margin-top:4px;font-size:5px;color:#888}
</style>
</head>
<body>
<div class="page">
  <div class="abs topbar"></div>

  <div class="abs brand"><span class="brand-mark"></span><span class="brand-name">Tidy Haven</span></div>
  <div class="abs brand-tag">Quality Commercial &amp; Residential Cleaning</div>

  <div class="abs callout">Call us Today and schedule your<br>FREE consultation and estimate! They are ALWAYS free!<span class="phone">(505) 555-0142</span></div>
  <div class="abs search">
    <svg width="7" height="7" viewBox="0 0 10 10"><circle cx="4" cy="4" r="3" fill="none" stroke="#f7941d" stroke-width="1.5"/><path d="M6.5 6.5L9 9" stroke="#f7941d" stroke-width="1.5"/></svg>
    Search Keyword
  </div>

  <div class="abs hero" role="img" aria-label="Bright luxury bedroom with white bedding opening onto a turquoise ocean view"></div>
  <nav class="abs nav">
    <a class="current">Home</a><a>Services</a><a>Employees</a><a>Why Choose Us?</a><a>Testimonials</a><a>Special Offers</a><a>About Us</a><a>Contact Us</a><a>Request a Bid</a><a>Meet The President</a>
  </nav>
  <div class="abs hero-caption"><span>Wouldn't it be nice,</span><br><span>To come home to a perfectly clean house?</span></div>

  <section class="abs about">
    <h2>About <em>Company</em></h2>
    <p>Thank you for visiting us! You are one step closer to experiencing first class maid service! Our company specializes in detailed housekeeping, janitorial, and commercial cleaning services making your environment shine and sparkle like it never has before! Our maids are fully trained professionals who we recruit from high end luxury hotels we know, like the Grandview and Harborline!</p>
    <p>We pride ourselves in delivering exceptional service to our valued customers by fully understanding what your expectations &amp; needs are! We will strive for perfection and we will provide an uncompromising commitment to excellence!</p>
    <a class="more">Learn More</a>
  </section>

  <h2 class="abs video-title">Video <em>Gallery</em></h2>
  <div class="abs video">
    <div class="video-frame" role="img" aria-label="Video still of a cleaner wiping a kitchen counter"></div>
    <div class="video-bar">
      <svg width="6" height="6" viewBox="0 0 6 6"><path d="M0 0L6 3L0 6Z" fill="#fff"/></svg>
      <span class="track"></span>
      <svg width="14" height="4"><rect width="14" height="3" fill="#4a8fc4"/></svg>
    </div>
  </div>

  <div class="abs band">Locally Owned &amp; Operated Never deal with an unresponsive franchise - Deal with the owner!</div>

  <article class="abs service" style="left:234px">
    <div class="thumb" role="img" aria-label="Office tower against a blue sky" style="background:linear-gradient(160deg,#9cc3e6,#5f7f9c)"></div>
    <h3>Commercial &amp; Office</h3>
    <p>Isn't easier to work in a nice clean office!?! We will make your facility sparkle like</p>
  </article>
  <article class="abs service" style="left:346px">
    <div class="thumb" role="img" aria-label="Dark modern kitchen interior" style="background:linear-gradient(160deg,#6b4a32,#2d1d12)"></div>
    <h3>Residential</h3>
    <p>Do you remember coming home from school and walking into your house and it smelled so clean</p>
  </article>
  <article class="abs service" style="left:458px">
    <div class="thumb" role="img" aria-label="Floor scattered with party confetti" style="background:linear-gradient(160deg,#d88a3a,#9c4a1c)"></div>
    <h3>Special Events</h3>
    <p>Have you ever thrown a huge party and some how when its all done and over with you are left</p>
  </article>
  <article class="abs service promo" style="left:570px">
    <div class="thumb" role="img" aria-label="Person sorting a pile of laundry" style="background:linear-gradient(160deg,#f1eee9,#b8c2cc)"></div>
    <h3>Is this how you feel sometimes?</h3>
    <p>Now offering laundry service for any customer! Included in your quote! Ask your account representative for details!</p>
    <strong>Full Laundry Services for all Customers at NO extra charge!</strong>
  </article>

  <div class="abs rule" style="top:650px"></div>

  <section class="abs clients">
    <h2>From <em>Clients</em></h2>
    <div class="slider"><span></span><span></span></div>
    <blockquote class="quote">
      <svg width="11" height="11" viewBox="0 0 12 12"><circle cx="6" cy="6" r="5.3" fill="none" stroke="#555" stroke-width="1"/><text x="6" y="8.6" font-size="7" text-anchor="middle" fill="#555" font-family="Arial">“</text></svg>
      <p>I was very impressed with the amount they do for the price! Remarkable! Thank you Tidy Haven for taking this daily headache away from my fiance. She was so thrilled. See you guys again soon!</p>
      <footer>Dana Whitfield <i>January 2, 2014</i></footer>
    </blockquote>
  </section>

  <section class="abs offer" style="left:234px;width:200px">
    <h2>Our <em>Commercial</em></h2>
    <p>Isn't easier to work in a nice clean office!?! We will make your facility sparkle like new so your guests and clients have a nice clean area when they visit [...]</p>
    <ul><li>Trash disposal</li><li>Sweeping &amp; Mopping</li><li>Clean and Replenish bathrooms</li><li>Full office clean with furniture shine</li><li>Window washing</li><li>Outside trash removal</li></ul>
  </section>
  <section class="abs offer" style="left:491px;width:185px">
    <h2>Our <em>Residential</em></h2>
    <p>Do you remember coming home from school and walking into your house and it smelled so clean, fresh, crisp, and it just gave you just really didnt want to touch [...]</p>
    <ul><li>Disinfecting</li><li>Pet baths &amp; minor grooming</li><li>Ceiling fan dusting</li><li>Dusting &amp; polishing</li><li>Fireplace cleaning</li><li>Organizing</li><li>Laundry cleaning &amp; folding</li></ul>
  </section>

  <div class="abs rule" style="top:908px"></div>

  <div class="abs pledges">
    <div class="pledge"><span class="badge"></span><span><b>Tidy Haven</b> is committed to using <b>Eco Green</b> chemicals to keep you and your family safe! No harsh chemicals here!</span></div>
    <div class="pledge">
      <svg width="16" height="26" viewBox="0 0 16 26" style="flex:none"><path d="M8 2C3 2 3 9 8 13C13 9 13 2 8 2ZM8 13L2 24M8 13L14 24" fill="none" stroke="#ddd" stroke-width="2.4"/></svg>
      <span>Tidy Haven proudly <b>donates 1%</b> of its earnings to find a cure for breast cancer! Be part of a life changing cause!</span></div>
    <div class="pledge"><span class="badge" style="background:#ccc"></span><span>We guarantee you will be <b>100% satisfied</b> with our cleaning and our cleaning professionals!</span></div>
  </div>

  <div class="abs rule" style="top:998px"></div>
  <div class="abs up"><svg width="14" height="14" viewBox="0 0 14 14"><path d="M4.5 8L7 5.5L9.5 8" fill="none" stroke="#fff" stroke-width="1.2"/></svg></div>

  <footer class="abs footer">
    <div class="fcol" style="left:234px;width:150px">
      <h4>Latest <em>Tweets</em></h4>
      <p style="margin-top:14px">Tidy Haven start getting more dollar!</p><span class="time">20 min ago</span>
      <p>Tidy Haven start getting more dollar!<br><span class="link">http://tidy.example/news</span></p><span class="time">20 min ago</span>
    </div>
    <div class="fcol" style="left:403px;width:120px">
      <h4>Social <em>Links</em></h4>
      <div class="row" style="margin-top:14px"><span class="dot" style="width:4px"></span>Find us on FriendSpace</div>
      <div class="row"><span class="dot" style="width:4px"></span>Get in ChirpLine</div>
    </div>
    <div class="fcol" style="left:536px;width:140px">
      <h4>Contact <em>Us</em></h4>
      <p style="margin-top:14px;color:#fff">Tidy Haven</p>
      <div class="row"><svg width="7" height="9" viewBox="0 0 7 9" style="flex:none"><path d="M3.5 0C1.5 0 0 1.5 0 3.4C0 6 3.5 9 3.5 9S7 6 7 3.4C7 1.5 5.5 0 3.5 0Z" fill="#f7941d"/><circle cx="3.5" cy="3.4" r="1.2" fill="#3a3a3a"/></svg><span>4120 Juniper Crest Ave Suite 310<br>Riverton , New Mexico - 87000</span></div>
      <div class="row"><span class="dot" style="border-radius:50%"></span>(505) 555-0142</div>
      <div class="row"><span class="dot" style="border-radius:50%"></span>(505) 555-0178</div>
      <div class="row"><span class="dot" style="height:5px;margin-top:1px"></span>hello@tidyhaven.example</div>
    </div>
  </footer>

  <div class="abs copy">
    <a class="current">Home</a> | <a>Services</a> | <a>Employees</a> | <a>Why Choose Us?</a> | <a>Testimonials</a> | <a>Special Offers</a> | <a>About Us</a> | <a>Contact Us</a> | <a>Request a Bid</a> | <a>Meet The President</a>
    <small>All Right Reserved 2014</small>
  </div>
</div>
</body>
</html>
```